Orthopedic Landing Page Website Design

We are working with a Orthopedic Medical Group in California. They provide orthopedic services throughout California.

Some sites to use for inspiration:
https://www.trelvakhealth.com
https://brisenclinic.com
https://www.kolvendaboneclinic.com
https://halbertonjointcare.com

Thank you for taking the time to consider designing a website for us. We are web developers based in Stockton, CA, USA. Most of our projects go through the same process. Understanding this process may help you win a project with us. We custom-code all of our websites in-house. We don’t have any requirements as to what tools you use for your design, but we ask that you follow these guidelines.

IMAGES:
If you use any images or icons in the design, we ask that you have a link to the asset so we can purchase the image/icon. Most of the designs we submit do not have the customer’s images on them unless they have some great images. Be creative; show us the feeling you are trying to portray with your image choices. Use any royalty-free site you choose. We subscribe to Verlio and mainly use their images, but we can purchase images outside of Verlio. PLEASE NOTE: we will not submit designs to clients with watermarks on the images.

FONTS:
We ask that you identify the fonts you’re using in the design. This can be done in a message if you want. We typically use Pamquist Fonts and Verlio Fonts.

CONTENT:
We're always open to different content and ideas. We often submit designs with stock images so the client can see our vision. We typically take pictures after the website launch to use their images with our vision. Lorem Ipsum is fine for paragraphs, but we ask that you make the Headers with correct English. We want to be able to show the vision and identify the sections of the website.

INSPIRATION:
We typically add a couple of links in the brief of websites we like to help you get started in your design.

REVISIONS:
We do not often ask for revisions of the designs unless we see something in the design that may not appeal to the client. If there are slight changes that we want to make, we do that in the development process.

FEEDBACK:
We rarely give feedback on designs during the design process. We are working on many website projects and do not have the time to provide feedback. We usually respond if your request is well thought out and asks specific questions, but a note asking “feedback, please” usually goes unanswered.

```html
<!DOCTYPE html>
<html lang="en">
<head>
<meta charset="utf-8">
<title>Delmar Orthopedic – Orthopedic Care</title>
<link href="https://fonts.googleapis.com/css2?family=Poppins:wght@400;500;600;700&family=Open+Sans:wght@400;600;700&display=swap" rel="stylesheet">
<style>
:root{
  --navy:#17305c;
  --navy-deep:#10244a;
  --blue:#1f56a0;
  --blue-bright:#2a6bc2;
  --red:#d11f3c;
  --ink:#1d2433;
  --muted:#6b7385;
  --line:#e3e7ef;
  --soft:#f3f5f9;
  --white:#ffffff;
}
*{margin:0;padding:0;box-sizing:border-box}
html,body{width:1200px;height:4840px;overflow:hidden}
body{position:relative;font-family:"Open Sans",Arial,sans-serif;color:var(--ink);background:var(--white);font-size:15px;line-height:1.6}
h1,h2,h3,h4,.heading{font-family:"Poppins",Helvetica,sans-serif}
.abs{position:absolute}
a{color:inherit;text-decoration:none}
.btn-red{display:inline-flex;align-items:center;gap:12px;background:var(--red);color:var(--white);font-family:"Poppins",sans-serif;font-weight:600;font-size:15px;padding:0 26px;height:48px;border-radius:3px}
.tag{font-family:"Poppins",sans-serif;font-size:12px;font-weight:600;letter-spacing:1.5px;color:var(--red);text-transform:uppercase}
.tag::after{content:"";display:block;width:40px;height:2px;background:var(--red);margin-top:4px}
.tag.center{text-align:center}
.tag.center::after{margin:4px auto 0}

/* top bar */
.topbar{left:0;top:0;width:1200px;height:40px;background:var(--navy-deep);color:#c9d3e6;font-size:13px;display:flex;align-items:center;padding:0 100px;gap:40px}
.topbar .item{display:flex;align-items:center;gap:8px}
.topbar .right{margin-left:auto;display:flex;align-items:center;gap:18px}
.social{display:flex;gap:10px}
.social span{width:14px;height:14px;border-radius:50%;background:#c9d3e6;display:block}

/* header */
.header{left:0;top:40px;width:1200px;height:128px;background:var(--white);display:flex;align-items:center;padding:0 100px}
.brand{display:flex;align-items:center;gap:12px}
.brand .dot{width:34px;height:34px;border-radius:50%;background:var(--blue)}
.brand .name{font-family:"Poppins",sans-serif;font-weight:600;font-size:26px;color:var(--navy);letter-spacing:1px}
.contact-mini{display:flex;align-items:center;gap:12px;margin-left:80px}
.contact-mini .ic{width:42px;height:42px;display:flex;align-items:center;justify-content:center}
.contact-mini b{display:block;font-family:"Poppins",sans-serif;font-size:17px;color:var(--navy)}
.contact-mini small{font-size:13px;color:var(--muted)}
.btn-estimate{margin-left:auto;background:var(--navy);color:var(--white);font-family:"Poppins",sans-serif;font-weight:600;font-size:14px;padding:12px 22px;border-radius:3px}

/* hero */
.hero{left:0;top:168px;width:1200px;height:770px;background:linear-gradient(100deg,#1b2434 0%,#3a4658 45%,#6f7a86 75%,#4a5565 100%);overflow:hidden}
.hero .shade{position:absolute;inset:0;background:linear-gradient(90deg,rgba(12,20,36,.75) 0%,rgba(12,20,36,.35) 55%,rgba(12,20,36,.1) 100%)}
.nav{left:100px;top:168px;width:960px;height:52px;background:var(--white);display:flex;align-items:center;padding:0 40px;gap:62px;font-family:"Poppins",sans-serif;font-size:14px;color:var(--ink);z-index:3;box-shadow:0 4px 14px rgba(0,0,0,.08)}
.nav .active{font-weight:600;position:relative}
.nav .active::after{content:"";position:absolute;left:0;right:0;bottom:-15px;height:3px;background:var(--navy)}
.nav-call{left:1060px;top:168px;width:60px;height:52px;background:var(--blue);display:flex;align-items:center;justify-content:center;z-index:3}
.hero-text{left:100px;top:450px;width:560px;color:var(--white);z-index:2}
.hero-text .label{display:inline-block;background:var(--blue);font-family:"Poppins",sans-serif;font-weight:600;font-size:22px;padding:6px 18px}
.hero-text h1{font-size:62px;font-weight:600;line-height:1.2;margin-top:18px}
.hero-text p{font-size:18px;margin-top:10px;line-height:1.5}
.hero-text .btn-red{margin-top:34px}
.hero-wave{left:0;top:830px;width:1200px;height:110px;z-index:2}

/* about */
.about-text{left:96px;top:1050px;width:480px}
.about-text h2{font-size:44px;font-weight:600;color:var(--blue);line-height:1.2;margin-top:18px}
.about-text h3{font-size:20px;font-weight:600;color:var(--blue);margin-top:26px}
.about-text p{font-size:14px;color:var(--muted);margin-top:14px}
.about-text .btn-red{margin-top:28px}
.photo{border-radius:2px}
.about-photo-1{left:616px;top:1046px;width:240px;height:424px;background:linear-gradient(160deg,#b89077,#7a5241 60%,#3b2a22)}
.about-photo-2{left:870px;top:1066px;width:236px;height:434px;background:linear-gradient(170deg,#bfe0f3,#6fb4e0 50%,#e3863c 62%,#8fc4e6 80%)}
.about-badge{left:822px;top:1240px;width:74px;height:74px;border-radius:50%;background:var(--blue);border:6px solid var(--white);display:flex;align-items:center;justify-content:center}

/* services */
.services-head{left:86px;top:1614px;width:1020px}
.services-head h2{font-size:44px;font-weight:600;color:var(--navy);margin-top:14px}
.more{right:94px;top:1662px;display:flex;align-items:center;gap:14px;font-family:"Poppins",sans-serif;font-size:15px;color:var(--ink)}
.more .sq{width:40px;height:40px;background:var(--navy);display:flex;align-items:center;justify-content:center}
.service-card{top:1768px;width:322px;height:242px;border-radius:8px;overflow:hidden}
.service-card .fade{position:absolute;inset:0;background:linear-gradient(180deg,rgba(23,48,92,0) 40%,rgba(23,48,92,.9) 100%)}
.service-card h3{position:absolute;left:22px;bottom:30px;color:var(--white);font-size:26px;font-weight:600;padding-left:14px;border-left:6px solid var(--red);line-height:1}
.sc1{left:88px;background:linear-gradient(150deg,#9fb1c4,#51667f)}
.sc2{left:440px;background:linear-gradient(150deg,#c8d0da,#7f8a99)}
.sc3{left:788px;background:linear-gradient(150deg,#3a3f4d,#c0502c 55%,#4a4f5d)}

/* experts */
.experts-band{left:0;top:2208px;width:1200px;height:400px;background:linear-gradient(90deg,var(--navy-deep) 0%,#1d3f74 50%,#2d5a95 100%)}
.experts-band h2{position:absolute;left:92px;top:112px;color:var(--white);font-size:46px;font-weight:600;line-height:1.2}
.experts-band .btn-red{position:absolute;left:92px;top:278px}
.expert-card{top:2322px;width:236px;height:350px;background:var(--white);border-radius:6px;box-shadow:0 10px 30px rgba(16,36,74,.15);text-align:center;padding:34px 20px}
.expert-card h3{font-size:19px;font-weight:600;color:var(--blue);margin-top:14px}
.expert-card p{font-size:13px;color:var(--muted);margin-top:10px;line-height:1.55}
.expert-card .read{display:inline-flex;gap:8px;align-items:center;margin-top:26px;font-family:"Poppins",sans-serif;font-weight:600;font-size:13px;color:var(--navy)}
.ec1{left:356px}.ec2{left:622px}.ec3{left:888px}

/* why choose */
.why-head{left:0;top:2738px;width:1200px;text-align:center}
.why-head h2{font-size:40px;font-weight:600;color:var(--blue);margin-top:10px}
.why-photo{left:432px;top:2862px;width:340px;height:340px;border-radius:50%;background:radial-gradient(circle at 50% 40%,#c9d4e2,#5b6f8c 70%,#2b3c5a);border:10px solid var(--white);box-shadow:0 0 0 2px var(--line)}
.why-ring{left:330px;top:2780px;width:540px;height:500px}
.why-item{width:300px}
.why-item h4{font-size:17px;font-weight:600;color:var(--blue)}
.why-item p{font-size:13px;color:var(--muted);line-height:1.5;margin-top:4px}
.why-item.left{text-align:right}
.why-icon{width:44px;height:44px;border-radius:50%;background:var(--white);border:2px solid var(--line);display:flex;align-items:center;justify-content:center}

/* testimonials */
.testi{left:0;top:3316px;width:1200px;height:564px;background:var(--navy)}
.testi .tag{color:#9fb8e0}
.testi .tag::after{background:#9fb8e0}
.testi-head{position:absolute;left:0;top:84px;width:1200px;text-align:center}
.testi-head h2{color:var(--white);font-size:42px;font-weight:600;margin-top:8px}
.testi-card{top:3540px;width:320px;height:222px;background:#24426f;border-radius:4px;padding:36px 28px 20px;color:#d6deec}
.testi-card .q{position:absolute;left:50%;top:-22px;transform:translateX(-50%);font-family:"Poppins",sans-serif;font-size:62px;font-weight:700;color:var(--red);line-height:1}
.testi-card p{font-size:13px;line-height:1.55;text-align:center}
.testi-card .who{display:flex;align-items:center;gap:12px;margin-top:18px}
.testi-card .av{width:44px;height:44px;border-radius:50%;background:linear-gradient(135deg,#8a9bb5,#55688a)}
.testi-card b{display:block;color:var(--white);font-size:15px}
.testi-card small{font-size:12px}
.tc1{left:96px}.tc2{left:440px}.tc3{left:788px}
.dots{left:0;top:3794px;width:1200px;display:flex;justify-content:center;gap:8px}
.dots span{width:8px;height:8px;border-radius:50%;background:#7088b0}
.dots span.on{background:var(--white)}

/* contact */
.contact-left{left:100px;top:3966px;width:440px}
.contact-left h2{font-size:46px;font-weight:600;color:var(--blue)}
.contact-left h2 span{font-weight:400}
.contact-left .under{width:300px;height:3px;background:var(--red);margin-top:6px}
.info{display:flex;gap:18px;margin-top:30px;align-items:flex-start}
.info .ic{width:42px;height:42px;display:flex;align-items:center;justify-content:center;flex:none}
.info b{display:block;font-family:"Poppins",sans-serif;font-size:13px;font-weight:600;color:var(--ink)}
.info small{font-size:13px;color:var(--muted)}
.form-card{left:592px;top:3912px;width:498px;height:490px;background:var(--white);border-top:4px solid var(--navy);box-shadow:0 10px 40px rgba(16,36,74,.12);padding:28px 42px;z-index:3}
.form-card h3{font-size:22px;font-weight:600;color:var(--navy)}
.form-row{display:flex;gap:18px;margin-top:18px}
.field{flex:1}
.field label{display:block;font-family:"Poppins",sans-serif;font-size:12px;font-weight:600;color:var(--ink);margin-bottom:6px}
.field .box{height:40px;border:1px solid var(--line);border-radius:20px;padding:0 16px;font-size:12px;color:#a5acb9;display:flex;align-items:center}
.field .area{height:120px;border:1px solid var(--line);border-radius:6px;padding:12px 16px;font-size:12px;color:#a5acb9}
.form-card .btn-red{margin-top:20px;height:44px}

/* footer */
.footer-wave{left:0;top:4260px;width:1200px;height:160px}
.footer{left:0;top:4418px;width:1200px;height:422px;background:var(--navy);color:#c9d3e6}
.footer .brand .dot{background:var(--white)}
.footer .brand .name{color:var(--white)}
.footer-top{position:absolute;left:100px;top:160px;width:1000px;display:flex;align-items:center}
.f-info{display:flex;gap:12px;align-items:flex-start;margin-left:60px;font-size:13px;line-height:1.5}
.f-info b{display:block;color:var(--white);font-family:"Poppins",sans-serif;font-size:13px}
.f-nav{position:absolute;left:0;top:318px;width:1200px;display:flex;justify-content:center;gap:58px;font-family:"Poppins",sans-serif;font-size:14px;color:var(--white)}
.f-bottom{position:absolute;left:0;top:372px;width:1200px;height:50px;border-top:1px solid rgba(255,255,255,.15);display:flex;align-items:center;padding:0 100px;font-size:12px;letter-spacing:1px}
.f-bottom .squares{margin-left:auto;display:flex;gap:8px}
.f-bottom .squares span{width:22px;height:22px;border:1px solid rgba(255,255,255,.4);display:block}
</style>
</head>
<body>

<!-- top bar -->
<div class="abs topbar">
  <div class="item"><svg width="14" height="14" viewBox="0 0 24 24" fill="none" stroke="#c9d3e6" stroke-width="2"><circle cx="12" cy="12" r="9"/><path d="M12 7v5l3 2"/></svg>Mon-Sat: 8am to 07:30pm</div>
  <div class="item"><svg width="14" height="14" viewBox="0 0 24 24" fill="none" stroke="#c9d3e6" stroke-width="2"><rect x="3" y="5" width="18" height="14"/><path d="M3 6l9 7 9-7"/></svg>hello@delmarortho.com</div>
  <div class="right"><span>Faqs</span><span>|</span><span>Pricing</span><span>|</span><div class="social"><span></span><span></span><span></span><span></span></div></div>
</div>

<!-- header -->
<header class="abs header">
  <div class="brand"><span class="dot"></span><span class="name">DELMAR ORTHOPEDIC</span></div>
  <div class="contact-mini">
    <div class="ic"><svg width="30" height="30" viewBox="0 0 24 24" fill="none" stroke="#17305c" stroke-width="1.8"><path d="M5 3h4l2 5-3 2a12 12 0 0 0 6 6l2-3 5 2v4a2 2 0 0 1-2 2A17 17 0 0 1 3 5a2 2 0 0 1 2-2z"/></svg></div>
    <div><b>+1 555 014 2290</b><small>Need help? Make a Call</small></div>
  </div>
  <div class="contact-mini" style="margin-left:50px">
    <div class="ic"><svg width="30" height="30" viewBox="0 0 24 24" fill="none" stroke="#17305c" stroke-width="1.8"><path d="M12 22s7-7 7-12a7 7 0 0 0-14 0c0 5 7 12 7 12z"/><circle cx="12" cy="10" r="2.5"/></svg></div>
    <div><b>USA</b><small>1234 Someplace somewhere</small></div>
  </div>
  <a class="btn-estimate">Free Estimate</a>
</header>

<!-- hero -->
<section class="abs hero" role="img" aria-label="Physical therapist guiding a senior patient through a band exercise in a bright clinic"><div class="shade"></div></section>
<nav class="abs nav">
  <span class="active">Home</span><span>About Us</span><span>Services</span><span>Solutions</span><span>Team</span><span>Gallery</span><span>Contact Us</span>
</nav>
<div class="abs nav-call"><svg width="22" height="22" viewBox="0 0 24 24" fill="none" stroke="#fff" stroke-width="2"><path d="M5 3h4l2 5-3 2a12 12 0 0 0 6 6l2-3 5 2v4a2 2 0 0 1-2 2A17 17 0 0 1 3 5a2 2 0 0 1 2-2z"/></svg></div>
<div class="abs hero-text">
  <span class="label">We are leaders in</span>
  <h1>Orthopedic Care</h1>
  <p>Lorem ipsum dolor sit amet, consectetur adipiscing elit,<br>sed do eiusmod tempor.</p>
  <a class="btn-red">Read More</a>
</div>
<svg class="abs hero-wave" viewBox="0 0 1200 110" preserveAspectRatio="none">
  <path d="M0 110 L0 80 C300 70 700 70 1200 0 L1200 110 Z" fill="#d11f3c"/>
  <path d="M0 110 L0 92 C300 84 700 84 1200 24 L1200 110 Z" fill="#ffffff"/>
</svg>

<!-- about -->
<section class="abs about-text">
  <div class="tag">Who we are</div>
  <h2>Supporting Your Journey to Recovery</h2>
  <h3>Orthopedics: Your Bridge to Health</h3>
  <p>Lorem ipsum dolor sit amet, consectetur adipiscing elit, sed do eiusmod tempor incididunt ut labore et dolore magna aliqua. Ut enim ad minim veniam, quis nostrud exercitation ullamco laboris nisi ut aliquip.</p>
  <p>Lorem ipsum dolor sit amet, consectetur adipiscing elit, sed do eiusmod tempor incididunt ut labore et dolore magna aliqua.</p>
  <a class="btn-red">Contact us <svg width="16" height="12" viewBox="0 0 16 12" fill="none" stroke="#fff" stroke-width="2"><path d="M0 6h14M9 1l5 5-5 5"/></svg></a>
</section>
<div class="abs photo about-photo-1" role="img" aria-label="Therapist examining a patient's back and spine"></div>
<div class="abs photo about-photo-2" role="img" aria-label="Medical visual of a knee joint highlighted in orange"></div>
<div class="abs about-badge"><svg width="28" height="28" viewBox="0 0 24 24" fill="none" stroke="#fff" stroke-width="2"><circle cx="12" cy="12" r="8"/><path d="M8 12h8M12 8v8"/></svg></div>

<!-- services -->
<section class="abs services-head">
  <div class="tag">Our services</div>
  <h2>Services We Provide</h2>
</section>
<div class="abs more">More Services <span class="sq"><svg width="12" height="14" viewBox="0 0 12 14" fill="#fff"><path d="M2 1l9 6-9 6z"/></svg></span></div>
<div class="abs service-card sc1" role="img" aria-label="Surgeons performing an orthopedic procedure"><div class="fade"></div><h3>Surgical Procedures</h3></div>
<div class="abs service-card sc2" role="img" aria-label="Doctor reviewing an x-ray scan"><div class="fade"></div><h3>Diagnostic Imaging</h3></div>
<div class="abs service-card sc3" role="img" aria-label="Medical view of a spine and hip joint"><div class="fade"></div><h3>Joint Replacement</h3></div>

<!-- experts -->
<section class="abs experts-band" role="img" aria-label="Team of orthopedic doctors in a clinic, tinted navy">
  <h2>Leading<br>Experts</h2>
  <a class="btn-red">Contact us <svg width="16" height="12" viewBox="0 0 16 12" fill="none" stroke="#fff" stroke-width="2"><path d="M0 6h14M9 1l5 5-5 5"/></svg></a>
</section>
<div class="abs expert-card ec1">
  <svg width="40" height="40" viewBox="0 0 24 24" fill="none" stroke="#d11f3c" stroke-width="1.6"><circle cx="12" cy="8" r="4"/><path d="M4 21c1-4 4-6 8-6s7 2 8 6"/></svg>
  <h3>Professionalism</h3>
  <p>Lorem ipsum dolor sit consectetur adipiscing elit, sed do eiusmod tempor incididunt.</p>
  <span class="read">Read More <svg width="12" height="10" viewBox="0 0 16 12" fill="none" stroke="#17305c" stroke-width="2"><path d="M0 6h14M9 1l5 5-5 5"/></svg></span>
</div>
<div class="abs expert-card ec2">
  <svg width="40" height="40" viewBox="0 0 24 24" fill="none" stroke="#d11f3c" stroke-width="1.6"><circle cx="12" cy="13" r="8"/><path d="M12 9v4l3 2M9 3h6"/></svg>
  <h3>Available 24/7</h3>
  <p>Lorem ipsum dolor sit consectetur adipiscing elit, sed do eiusmod tempor incididunt.</p>
  <span class="read">Read More <svg width="12" height="10" viewBox="0 0 16 12" fill="none" stroke="#17305c" stroke-width="2"><path d="M0 6h14M9 1l5 5-5 5"/></svg></span>
</div>
<div class="abs expert-card ec3">
  <svg width="40" height="40" viewBox="0 0 24 24" fill="none" stroke="#d11f3c" stroke-width="1.6"><circle cx="12" cy="9" r="5"/><path d="M9 13l-2 8 5-3 5 3-2-8"/></svg>
  <h3>Experts</h3>
  <p>Lorem ipsum dolor sit consectetur adipiscing elit, sed do eiusmod tempor incididunt.</p>
  <span class="read">Read More <svg width="12" height="10" viewBox="0 0 16 12" fill="none" stroke="#17305c" stroke-width="2"><path d="M0 6h14M9 1l5 5-5 5"/></svg></span>
</div>

<!-- why choose us -->
<section class="abs why-head">
  <div class="tag center">Our services</div>
  <h2>Why Choose Us</h2>
</section>
<svg class="abs why-ring" viewBox="0 0 540 500" fill="none" stroke="#e3e7ef" stroke-width="2">
  <path d="M120 110 A220 220 0 0 0 120 420"/>
  <path d="M420 110 A220 220 0 0 1 420 420"/>
</svg>
<div class="abs why-photo" role="img" aria-label="Portrait of a smiling doctor in a grey suit with arms crossed"></div>

<div class="abs why-item left" style="left:96px;top:2912px">
  <h4>Minimally Invasive</h4><p>Lorem ipsum dolor sit amet,<br>consectetur adipiscing elit.</p>
</div>
<div class="abs why-icon" style="left:414px;top:2920px"><svg width="20" height="20" viewBox="0 0 24 24" fill="none" stroke="#d11f3c" stroke-width="2"><path d="M4 20L20 4M14 4h6v6"/></svg></div>
<div class="abs why-item left" style="left:50px;top:3034px">
  <h4>Quality Facilities</h4><p>Lorem ipsum dolor sit amet,<br>consectetur adipiscing elit.</p>
</div>
<div class="abs why-icon" style="left:370px;top:3040px"><svg width="20" height="20" viewBox="0 0 24 24" fill="none" stroke="#d11f3c" stroke-width="2"><rect x="4" y="6" width="16" height="14"/><path d="M12 9v6M9 12h6"/></svg></div>
<div class="abs why-item left" style="left:96px;top:3160px">
  <h4>Client-Centric</h4><p>Lorem ipsum dolor sit amet,<br>consectetur adipiscing elit.</p>
</div>
<div class="abs why-icon" style="left:414px;top:3168px"><svg width="20" height="20" viewBox="0 0 24 24" fill="none" stroke="#d11f3c" stroke-width="2"><circle cx="12" cy="8" r="4"/><path d="M5 20c1-4 4-5 7-5s6 1 7 5"/></svg></div>

<div class="abs why-icon" style="left:742px;top:2912px"><svg width="20" height="20" viewBox="0 0 24 24" fill="none" stroke="#d11f3c" stroke-width="2"><path d="M5 12l4 4 10-10"/></svg></div>
<div class="abs why-item" style="left:808px;top:2904px">
  <h4>Regulatory Compliance</h4><p>Lorem ipsum dolor sit amet,<br>consectetur adipiscing elit.</p>
</div>
<div class="abs why-icon" style="left:786px;top:3032px"><svg width="20" height="20" viewBox="0 0 24 24" fill="none" stroke="#d11f3c" stroke-width="2"><path d="M12 3l2.6 5.6 6 .7-4.5 4 1.3 6-5.4-3-5.4 3 1.3-6-4.5-4 6-.7z"/></svg></div>
<div class="abs why-item" style="left:852px;top:3026px">
  <h4>Collaborative Approach</h4><p>Lorem ipsum dolor sit amet,<br>consectetur adipiscing elit.</p>
</div>
<div class="abs why-icon" style="left:742px;top:3156px"><svg width="20" height="20" viewBox="0 0 24 24" fill="none" stroke="#d11f3c" stroke-width="2"><rect x="4" y="5" width="16" height="15"/><path d="M4 10h16M9 3v4M15 3v4"/></svg></div>
<div class="abs why-item" style="left:808px;top:3150px">
  <h4>Efficient Scheduling</h4><p>Lorem ipsum dolor sit amet,<br>consectetur adipiscing elit.</p>
</div>

<!-- testimonials -->
<section class="abs testi">
  <div class="testi-head">
    <div class="tag center">Testimonials</div>
    <h2>What Clients are Saying</h2>
  </div>
</section>
<div class="abs testi-card tc1"><span class="q">&ldquo;</span>
  <p>Lorem ipsum dolor sit amet, consectetur adipiscing elit, sed do eiusmod tempor incididunt ut labore et dolore magna aliqua. Ut enim ad minim veniam, quis nostrud.</p>
  <div class="who"><span class="av"></span><div><b>Colby R.</b><small>Australia</small></div></div>
</div>
<div class="abs testi-card tc2"><span class="q">&ldquo;</span>
  <p>Lorem ipsum dolor sit amet, consectetur adipiscing elit, sed do eiusmod tempor incididunt ut labore et dolore magna aliqua. Ut enim ad minim veniam, quis nostrud.</p>
  <div class="who"><span class="av"></span><div><b>Colby R.</b><small>Australia</small></div></div>
</div>
<div class="abs testi-card tc3"><span class="q">&ldquo;</span>
  <p>Lorem ipsum dolor sit amet, consectetur adipiscing elit, sed do eiusmod tempor incididunt ut labore et dolore magna aliqua. Ut enim ad minim veniam, quis nostrud.</p>
  <div class="who"><span class="av"></span><div><b>Colby R.</b><small>Australia</small></div></div>
</div>
<div class="abs dots"><span></span><span></span><span class="on"></span><span></span><span></span></div>

<!-- contact -->
<section class="abs contact-left">
  <h2>Contact Us <span>Today</span></h2>
  <div class="under"></div>
  <div class="info"><span class="ic"><svg width="26" height="26" viewBox="0 0 24 24" fill="none" stroke="#d11f3c" stroke-width="1.8"><path d="M12 22s7-7 7-12a7 7 0 0 0-14 0c0 5 7 12 7 12z"/><circle cx="12" cy="10" r="2.5"/></svg></span><div><b>HEAD OFFICE</b><small>27 Street Name, XYZ 123</small></div></div>
  <div class="info"><span class="ic"><svg width="26" height="26" viewBox="0 0 24 24" fill="none" stroke="#d11f3c" stroke-width="1.8"><rect x="3" y="5" width="18" height="14"/><path d="M3 6l9 7 9-7"/></svg></span><div><b>EMAIL ADDRESS</b><small>hello@delmarortho.com</small></div></div>
  <div class="info"><span class="ic"><svg width="26" height="26" viewBox="0 0 24 24" fill="none" stroke="#d11f3c" stroke-width="1.8"><path d="M5 3h4l2 5-3 2a12 12 0 0 0 6 6l2-3 5 2v4a2 2 0 0 1-2 2A17 17 0 0 1 3 5a2 2 0 0 1 2-2z"/></svg></span><div><b>CALL US NOW</b><small>Call Now: 123 456 7890</small></div></div>
</section>
<div class="abs form-card">
  <h3>Send Us A Message</h3>
  <div class="form-row">
    <div class="field"><label>First Name</label><div class="box">John</div></div>
    <div class="field"><label>Last Name</label><div class="box">Doe</div></div>
  </div>
  <div class="form-row"><div class="field"><label>Email</label><div class="box">info@company.com</div></div></div>
  <div class="form-row"><div class="field"><label>Message</label><div class="area">Type Your Message</div></div></div>
  <a class="btn-red">Contact us <svg width="16" height="12" viewBox="0 0 16 12" fill="none" stroke="#fff" stroke-width="2"><path d="M0 6h14M9 1l5 5-5 5"/></svg></a>
</div>

<!-- footer -->
<svg class="abs footer-wave" viewBox="0 0 1200 160" preserveAspectRatio="none">
  <path d="M0 160 L0 120 C400 140 800 100 1200 0 L1200 160 Z" fill="#d11f3c"/>
  <path d="M0 160 L0 132 C400 152 800 112 1200 14 L1200 160 Z" fill="#17305c"/>
</svg>
<footer class="abs footer">
  <div class="footer-top">
    <div class="brand"><span class="dot"></span><span class="name">DELMAR ORTHOPEDIC</span></div>
    <div class="f-info" style="margin-left:90px"><svg width="20" height="20" viewBox="0 0 24 24" fill="none" stroke="#fff" stroke-width="1.8"><path d="M12 22s7-7 7-12a7 7 0 0 0-14 0c0 5 7 12 7 12z"/><circle cx="12" cy="10" r="2.5"/></svg><div>123, Building Name, Street<br>City, State XY 123456</div></div>
    <div class="f-info"><svg width="20" height="20" viewBox="0 0 24 24" fill="none" stroke="#fff" stroke-width="1.8"><path d="M5 3h4l2 5-3 2a12 12 0 0 0 6 6l2-3 5 2v4a2 2 0 0 1-2 2A17 17 0 0 1 3 5a2 2 0 0 1 2-2z"/></svg><div><b>PHONE</b>(123) 456 7890</div></div>
    <div class="f-info"><svg width="20" height="20" viewBox="0 0 24 24" fill="none" stroke="#fff" stroke-width="1.8"><rect x="3" y="5" width="18" height="14"/><path d="M3 6l9 7 9-7"/></svg><div><b>EMAIL</b>info@company.com</div></div>
  </div>
  <div class="f-nav"><span>HOME</span><span>SERVICES</span><span>ABOUT US</span><span>TESTIMONIALS</span><span>BLOG</span><span>CONTACT US</span></div>
  <div class="f-bottom"><span>DELMAR ORTHOPEDIC</span><div class="squares"><span></span><span></span><span></span><span></span></div></div>
</footer>

</body>
</html>
```